have uploaded pics of actual products I will use,here goes
Flapnora
honey butter complete mix 7.75 once $1.69
complete pancake mix 5.1 ounce $2.49
Milk
whole $4.44
C
Moonvessel coffee
medium blend 2.5 ounce $2.99
Qavo sugar
22 ounce pour container $3.49
Tarrowin's cereal
sold by the eaches
$1.29 each
any variety
Apple juice
pelby's 86 ounce bottle
(picture shows 2 bottles of 86 ounce juice)
Pelby's applesauce 3 pack 3 four ounce cups per pack
(picstues show 36 count in back, beeds edite)
Felix dorran turkey bacon 12 ounce pack $3.25
lantern coffee 2.5 ounce $2.50
whitlos eggnog one quart $2.99
rusty vale pre cooked hot and spicy 8 count 9.6 oz $4.49
rusty vale lnks 12 count 10 oz $4.49
Quenby silver crest 1 pound $7.98
Tarrowin fun size cereal 8 count 8.56oz $4.15
tillers gallon milk $4.44
whole, 1% and 2%
whitlos o.j 1 gallon $5.29 128 oz
verelle yogurt 6 oz
peach .69 each
strawberry .69 each
Halverton cinnamon rolls 5 count 7.3 ounce $1.99
Halverton plumps 5 big biscuits 10.2 oz $1.99
zelco hollow brook sharp 8 oz $3.99
zelco sharp shredded cheddar 8 oz $2.99
whitlos half and half 16 ounce $2.49
Thanks!
flyer and business card (which I would like to double as refrigerator magnet. should I increase money to $200 or leave at $150 and offer $50 for second place?
would appreciate all comments
maybe red or yellow
you want flyer or card ?

```html
<!DOCTYPE html>
<html lang="en">
<head>
<meta charset="utf-8">
<title>Dairy Sprite – Business Card 3.5 x 2</title>
<link rel="stylesheet" href="https://fonts.googleapis.com/css2?family=Open+Sans:wght@400;600;700;800&family=Comic+Neue:ital,wght@1,700&display=swap">
<style>
  :root {
    --navy: #1b3f95;
    --ink: #111111;
    --white: #ffffff;
    --yellow-light: #ffd21a;
    --yellow-deep: #f4a51c;
    --red-bright: #e4202a;
    --red-deep: #b3141e;
    --lime: #e8f73a;
    --genie-teal: #6fbfa8;
    --genie-purple: #7c5aa6;
  }
  * { margin: 0; padding: 0; box-sizing: border-box; }
  html, body {
    width: 1200px; height: 883px; overflow: hidden;
    background: var(--white);
    font-family: "Open Sans", Arial, sans-serif;
  }
  .canvas { position: relative; width: 1200px; height: 883px; }
  .size-label {
    position: absolute; top: 6px; left: 0; width: 100%;
    text-align: center; font-size: 44px; color: var(--ink); font-weight: 400;
  }
  .card {
    position: absolute; left: 0; top: 149px; width: 1200px; height: 734px;
    border-radius: 48px; overflow: hidden;
  }
  .card-bg { position: absolute; inset: 0; width: 100%; height: 100%; }
  .txt { position: absolute; white-space: nowrap; transform: translateX(-50%); line-height: 1; }
  .web { font-weight: 700; }
  .web--top { left: 569px; top: 72px; font-size: 26px; color: var(--navy); }
  .phone--top { left: 569px; top: 104px; font-size: 18px; color: var(--navy); font-weight: 700; }
  .tagline {
    left: 650px; top: 132px; font-size: 28px; color: var(--navy);
    font-family: "Comic Neue", "Comic Sans MS", cursive;
    font-style: italic; font-weight: 700;
    text-shadow: 0 0 3px var(--white), 0 0 3px var(--white);
  }
  .promise {
    left: 805px; top: 242px; font-size: 29px; color: var(--navy);
    font-family: "Comic Neue", "Comic Sans MS", cursive; font-style: italic; font-weight: 700;
    transform: translateX(-50%) rotate(-13deg);
  }
  .home-delivery { left: 890px; top: 358px; font-size: 28px; color: var(--white); }
  .schedule-box {
    position: absolute; left: 696px; top: 401px; width: 391px; height: 46px;
    background: var(--white); border-radius: 8px;
    display: flex; align-items: center; justify-content: center;
    font-size: 35px; font-weight: 700; color: var(--navy);
  }
  .days {
    position: absolute; left: 612px; top: 476px; width: 540px;
    display: flex; justify-content: space-between;
    color: var(--white); font-size: 30px; font-weight: 600;
  }
  .days .sep { opacity: .9; }
  .checks { position: absolute; left: 0; top: 523px; }
  .check {
    position: absolute; width: 34px; height: 34px;
    background: var(--white); border-radius: 6px;
  }
  .suppliers { left: 320px; top: 480px; font-size: 27px; color: var(--white); }
  .free-delivery {
    left: 290px; top: 555px; font-size: 46px; font-weight: 800;
    font-family: "Comic Neue", "Comic Sans MS", cursive; font-style: italic;
    color: var(--lime);
    -webkit-text-stroke: 2px var(--navy);
    transform: translateX(-50%) rotate(-8deg);
  }
  .minimum { left: 300px; top: 610px; font-size: 28px; color: var(--white); }
  .web--bottom { left: 600px; top: 620px; font-size: 29px; color: var(--white); font-weight: 400; }
  .phone--bottom { left: 600px; top: 660px; font-size: 19px; color: var(--white); font-weight: 700; }
  .genie-art { position: absolute; left: 66px; top: 22px; width: 340px; height: 350px; }
  .brand-mark {
    left: 150px; top: 100px; font-size: 15px; color: var(--white); font-weight: 700;
  }
</style>
</head>
<body>
<div class="canvas">
  <p class="size-label">business card 3,5 X 2”</p>

  <section class="card">
    <svg class="card-bg" viewBox="0 0 1200 734" preserveAspectRatio="none" aria-hidden="true">
      <defs>
        <linearGradient id="redField" x1="0" y1="0" x2="0" y2="1">
          <stop offset="0" stop-color="var(--red-deep)"/>
          <stop offset=".45" stop-color="var(--red-bright)"/>
          <stop offset="1" stop-color="var(--red-deep)"/>
        </linearGradient>
        <linearGradient id="yellowField" x1="0" y1="0" x2="1" y2="0.4">
          <stop offset="0" stop-color="var(--yellow-deep)"/>
          <stop offset=".6" stop-color="var(--yellow-light)"/>
          <stop offset="1" stop-color="var(--yellow-deep)"/>
        </linearGradient>
      </defs>
      <rect width="1200" height="734" fill="url(#redField)"/>
      <path d="M0,0 H880 C1010,10 1120,55 1200,95 V112 C1000,260 720,395 420,378 C260,368 110,352 0,346 Z" fill="url(#yellowField)"/>
      <path d="M420,378 C720,395 1000,260 1200,112 V150 C1000,300 720,420 420,398 Z" fill="var(--red-deep)" opacity=".35"/>
    </svg>

    <svg class="genie-art" viewBox="0 0 340 350" role="img" aria-label="Illustration of a friendly genie rising from a lamp, holding up a jug of milk, in front of a round blue badge">
      <defs>
        <linearGradient id="genieTone" x1="0" y1="0" x2="0" y2="1">
          <stop offset="0" stop-color="var(--genie-teal)"/>
          <stop offset="1" stop-color="var(--genie-purple)"/>
        </linearGradient>
      </defs>
      <ellipse cx="160" cy="175" rx="150" ry="168" fill="url(#genieTone)"/>
    </svg>
    <span class="txt brand-mark">dairysprite.com</span>

    <span class="txt web web--top">dairysprite.com</span>
    <span class="txt phone--top">1-866-moo-4512</span>
    <span class="txt tagline">delivered to your door before breakfast</span>
    <span class="txt promise">quality, fresh, fully guaranteed</span>

    <span class="txt home-delivery">free home delivery</span>
    <div class="schedule-box">delivery schedule</div>

    <div class="days">
      <span>Mon</span><span class="sep">|</span><span>Tue</span><span class="sep">|</span><span>Wed</span><span class="sep">|</span><span>Thu</span><span class="sep">|</span><span>Sat</span><span class="sep">|</span><span>Sun</span>
    </div>
    <div class="checks">
      <span class="check" style="left:634px"></span>
      <span class="check" style="left:729px"></span>
      <span class="check" style="left:818px"></span>
      <span class="check" style="left:902px"></span>
      <span class="check" style="left:986px"></span>
      <span class="check" style="left:1085px"></span>
    </div>

    <span class="txt suppliers">moonvessel, Tarrowin, zelco, dunnmere's</span>

    <span class="txt free-delivery">free delivery</span>
    <span class="txt minimum">only $10 min</span>

    <span class="txt web web--bottom">dairysprite.com</span>
    <span class="txt phone--bottom">1-866-moo-4512</span>
  </section>
</div>
</body>
</html>
```